Wedding Startup Full Website Design

We've just completed our online platform and need to create a website that represents our brand and vision, and clearly communicates our features and value proposition to potential users. There are a minimum of 4 pages that need to be designed. One geared toward wedding professionals (venues/vendors/coordinators), another toward engaged couples, one showcasing features, and an 'About Us' page.

The designer will creative freedom to create a unique UI/UX as long as it represents our brand and is relevant to our target audience/market. The ideal candidate will be able to assume the mindset of someone working in the wedding industry and/or an engaged couple. Ability to create illustrations is a plus.

Copy will be provided as needed. We will reimburse for stock images (pending approval before purchasing), but sourcing the stock images will be the responsibility of the designer.

Our current website: https://www.trelmora.com
Updates

Our project has now been guaranteed! We look forward to finding the perfect design for our site pages!

Still waiting for a design that stands out from the rest and aligns with the creative brief.

Target Market(s)

Wedding Professionals and Engaged Couples

Industry/Entity Type

Wedding

Number of Pages Required

4 page

Font styles to use
Sans Serif

Colors
ffffff
fbd4d5
f59195
33a6d7
cadf82
86cfc6

Requirements
Must have
• Common sense stuff like having a unified brand that accurately represents our platform, speaks to our target market, and clearly articulates our vision
Nice to have
• Illustrations
Should not have
• Overly cheesy or childish. We want to be professional but still embrace the wedding culture.

```html
<!DOCTYPE html>
<html lang="en">
<head>
<meta charset="utf-8">
<title>Trelmora — Wedding Planning Platform</title>
<link href="https://fonts.googleapis.com/css2?family=Pinyon+Script&family=Questrial&display=swap" rel="stylesheet">
<style>
:root{
  --white:#ffffff;
  --blush:#fbd4d5;
  --rose:#f59195;
  --rose-band:#f4999c;
  --sky:#33a6d7;
  --ink:#1c1c1c;
  --text:#555555;
  --line:#d9d9d9;
  --footer-bg:#f7f7f7;
  --script:"Pinyon Script", cursive;
  --sans:"Questrial", sans-serif;
}
*{margin:0;padding:0;box-sizing:border-box}
html,body{width:1200px;height:2174px;overflow:hidden;background:var(--white)}
body{position:relative;font-family:var(--sans);color:var(--text)}
.abs{position:absolute}

/* header */
.site-header{left:0;top:0;width:1200px;height:78px;background:var(--white)}
.brand{left:160px;top:18px;font-family:var(--sans);font-size:34px;line-height:42px;color:var(--sky)}
.main-nav{right:161px;top:32px;display:flex;gap:46px;font-size:12px}
.main-nav a{color:var(--ink);text-decoration:none}
.main-nav a.active{color:var(--sky)}

/* hero */
.hero{left:0;top:78px;width:1200px;height:582px;
  background:linear-gradient(180deg,rgba(255,255,255,0) 70%,#fff 100%),
  linear-gradient(100deg,#c9b9a6 0%,#e8dccd 30%,#f0ebe2 50%,#d8dcc4 70%,#a8b8b0 100%)}

/* section headings */
.script-title{font-family:var(--script);font-weight:400;color:var(--ink);text-align:center;width:1200px;left:0;line-height:1.2}
.why-title{top:714px;font-size:22px}

/* why band */
.why-band{left:161px;top:765px;width:878px;height:151px;background:var(--rose)}
.why-item{position:absolute;top:25px;width:113px;height:113px;border:2px solid var(--white);border-radius:50%;
  color:var(--white);font-size:10.5px;text-align:center;line-height:12px}
.why-item svg{position:absolute;left:50%;top:18px;transform:translateX(-50%)}
.why-item span{position:absolute;left:6px;right:6px;top:69px}

/* divider */
.divider{left:161px;width:878px;height:16px}
.divider .rule{position:absolute;top:7px;height:1px;width:405px;background:var(--line)}
.divider .rule.l{left:0}.divider .rule.r{right:0}
.divider svg{position:absolute;left:427px;top:0}
.features-title{top:1000px;font-size:20px;color:var(--rose)}

/* features */
.feature-heading{font-family:var(--script);font-weight:400;color:var(--ink);font-size:38px;line-height:38px}
.pro-heading{left:161px;top:1084px}
.couple-heading{right:161px;top:1084px;text-align:right}
.feature-copy{width:176px;font-size:11.5px;line-height:18.8px;color:var(--text)}
.pro-copy{left:161px;top:1186px}
.couple-copy{right:161px;top:1186px;text-align:right}
.photo{top:1066px;width:170px;height:218px}
.photo-pro{left:419px;background:linear-gradient(160deg,#5f7a5a,#cfc8bf 45%,#eeeae5)}
.photo-couple{left:612px;background:linear-gradient(160deg,#b8a58a,#7c5b4f 45%,#c8414a)}
.ornament{top:1284px;width:170px;height:64px;background:linear-gradient(180deg,#ececec,#fafafa)}
.ornament.a{left:419px}.ornament.b{left:612px}
.btn-learn{left:530px;top:1398px;width:138px;height:37px;border-radius:19px;background:var(--sky);
  color:var(--white);font-size:11px;text-align:center;line-height:37px;letter-spacing:.3px}

/* get started band */
.start-band{left:0;top:1526px;width:1200px;height:284px;
  background:linear-gradient(180deg,#f39a9d 0%,#f5a3a3 55%,#f7b0a6 80%,#f49a9c 100%)}
.start-title{top:1562px;font-size:40px}
.start-divider .rule{background:var(--white)}
.step{top:1672px;height:77px;border:2px solid var(--white);border-radius:3px;color:var(--white);padding:14px 20px 0}
.step h3{font-weight:400;font-size:15px;letter-spacing:.2px}
.step p{font-size:10.5px;line-height:14px;margin-top:3px}
.step.s1{left:161px;width:271px}.step.s2{left:464px;width:269px}.step.s3{left:768px;width:269px}

/* cta */
.cta-title{top:1876px;font-size:22px}
.cta-link{left:0;width:1200px;top:1910px;text-align:center;font-size:11px}
.cta-link a{color:var(--ink)}

/* footer */
.site-footer{left:0;top:1953px;width:1200px;height:221px;background:var(--footer-bg)}
.foot-col{text-align:center;font-size:10.5px;color:var(--ink)}
.foot-col h4{font-weight:400;font-size:11px;letter-spacing:.3px}
.foot-col h4::after{content:"";display:block;width:50px;height:2px;background:var(--ink);margin:7px auto 0}
.loc{left:134px;width:240px;top:1994px}
.loc p{line-height:22px}
.loc .first{margin-top:28px}
.foot-brand{left:0;width:1200px;top:2024px;text-align:center;font-size:36px;color:var(--sky);line-height:44px}
.copyright{left:0;width:1200px;top:2083px;text-align:center;font-size:10px;color:var(--ink)}
.touch{left:850px;width:200px;top:1994px}
.socials{left:874px;top:2052px;display:flex;gap:10px}
.socials span{width:26px;height:26px;border-radius:50%;background:var(--white);box-shadow:0 1px 3px rgba(0,0,0,.15)}
</style>
</head>
<body>

<header class="site-header abs">
  <div class="brand abs">Trelmora</div>
  <nav class="main-nav abs">
    <a class="active" href="#">Wedding Professionals</a>
    <a href="#">About Us</a>
    <a href="#">Features</a>
    <a href="#">For Couples</a>
  </nav>
</header>

<div class="hero abs" role="img" aria-label="Beach wedding ceremony with white floral arch, guests on white chairs and a bouquet of white roses in the foreground"></div>

<h2 class="script-title why-title abs">Why Trelmora</h2>
<section class="why-band abs">
  <div class="why-item" style="left:31px">
    <svg width="40" height="40" viewBox="0 0 40 40" fill="none" stroke="#fff" stroke-width="2.5"><circle cx="20" cy="20" r="16"/><path d="M20 10v10l7 5"/></svg>
    <span>Saves Everyone Time</span></div>
  <div class="why-item" style="left:205px">
    <svg width="44" height="40" viewBox="0 0 44 40" fill="none" stroke="#fff" stroke-width="2.5"><path d="M6 6h22v16H14l-6 6v-6H6z"/><path d="M30 14h8v14h-3v5l-5-5H18v-3"/></svg>
    <span>Better Client Reviews</span></div>
  <div class="why-item" style="left:380px">
    <svg width="40" height="40" viewBox="0 0 40 40" fill="none" stroke="#fff" stroke-width="2.5"><rect x="4" y="6" width="28" height="20"/><path d="M18 26v6M11 34h14"/><rect x="28" y="16" width="9" height="16" fill="#f59195"/></svg>
    <span>Accessible on Any Device</span></div>
  <div class="why-item" style="left:554px">
    <svg width="46" height="40" viewBox="0 0 46 40" fill="none" stroke="#fff" stroke-width="2.5"><rect x="17" y="4" width="12" height="9"/><rect x="9" y="16" width="12" height="9"/><rect x="25" y="16" width="12" height="9"/><rect x="2" y="28" width="12" height="9"/><rect x="17" y="28" width="12" height="9"/><rect x="32" y="28" width="12" height="9"/></svg>
    <span>Simplified Organization</span></div>
  <div class="why-item" style="left:730px">
    <svg width="44" height="40" viewBox="0 0 44 40" fill="none" stroke="#fff" stroke-width="2.5"><rect x="8" y="12" width="28" height="16"/><circle cx="22" cy="20" r="4"/><path d="M8 6h26l-4-4M36 34H10l4 4"/></svg>
    <span>Lower transaction Fees</span></div>
</section>

<div class="divider abs" style="top:982px"><i class="rule l"></i>
  <svg width="24" height="16" viewBox="0 0 24 16" fill="none" stroke="#f59195" stroke-width="1.4"><circle cx="8" cy="8" r="5"/><circle cx="16" cy="8" r="5"/></svg>
  <i class="rule r"></i></div>
<h2 class="script-title features-title abs">Trelmora Features</h2>

<h3 class="feature-heading pro-heading abs">For<br>Professional</h3>
<p class="feature-copy pro-copy abs">No longer do you have to go through emails, phone records, text messages, and meeting notes in order to piece together all the details for an upcoming event. With Trelmora, when clients make changes.</p>
<div class="photo photo-pro abs" role="img" aria-label="Wedding professional in shirt and tie seated at a desk"></div>
<div class="photo photo-couple abs" role="img" aria-label="Smiling engaged couple sitting together"></div>
<div class="ornament a abs" role="img" aria-label="Light grey lace ornament below the photo"></div>
<div class="ornament b abs" role="img" aria-label="Light grey lace ornament below the photo"></div>
<h3 class="feature-heading couple-heading abs">For<br>Couples</h3>
<p class="feature-copy couple-copy abs">No longer do you have to go through emails, phone records, text messages, and meeting notes in order to piece together all the details for an upcoming event. With Trelmora, when clients make changes.</p>
<a class="btn-learn abs">LEARN MORE</a>

<section class="start-band abs" role="img" aria-label="Soft pink background with blurred pink balloons along the bottom"></section>
<h2 class="script-title start-title abs">How To Get Started</h2>
<div class="divider start-divider abs" style="top:1625px"><i class="rule l"></i>
  <svg width="24" height="16" viewBox="0 0 24 16" fill="none" stroke="#fff" stroke-width="1.4"><circle cx="8" cy="8" r="5"/><circle cx="16" cy="8" r="5"/></svg>
  <i class="rule r"></i></div>
<div class="step s1 abs"><h3>SIGN UP</h3><p>Create a free account on Trelmora to access popular collaboration tools. Get Started</p></div>
<div class="step s2 abs"><h3>COLLABORATE</h3><p>Add clients within the application to better organize and manage event details.</p></div>
<div class="step s3 abs"><h3>CONNECT</h3><p>Linking your bank account within Trelmora to allow for seamless payments and monitoring.</p></div>

<div class="divider abs" style="top:1853px"><i class="rule l"></i>
  <svg width="24" height="16" viewBox="0 0 24 16" fill="none" stroke="#f59195" stroke-width="1.4"><circle cx="8" cy="8" r="5"/><circle cx="16" cy="8" r="5"/></svg>
  <i class="rule r"></i></div>
<h2 class="script-title cta-title abs">Get Started Today</h2>
<div class="cta-link abs"><a href="#">Access Demo</a></div>

<footer class="site-footer abs"></footer>
<div class="foot-col loc abs">
  <h4>LOCATION</h4>
  <p class="first">Lorem Ipsum Dolor Sit Amet Consect</p>
  <p>010 7788 4521</p>
  <p>info@trelmora.com</p>
</div>
<div class="foot-brand abs">Trelmora</div>
<div class="copyright abs">© Copyright 2018 trelmora, Allright reserved.</div>
<div class="foot-col touch abs"><h4>GET IN TOUCH</h4></div>
<div class="socials abs"><span></span><span></span><span></span><span></span><span></span></div>

</body>
</html>
```